Stationery for Public Accountant Practice

Name of Practice
Holloway Advisory Pty Ltd
Tel: 0417262938
Postal Address : PO Box 482, Elmsford Park, Vic 3187

Target Market(s)

Small Business Clients

Industry/Entity Type

Accounting

Font styles to use
Serif

Requirements
Must have
• Letterhead, business card, With compliments slip
Nice to have
• Conservative

```html
<!DOCTYPE html>
<html lang="en">
<head>
<meta charset="utf-8">
<title>Holloway Advisory — Stationery</title>
<link href="https://fonts.googleapis.com/css2?family=Cinzel:wght@400&family=Raleway:wght@300&family=Tinos:wght@400;700&family=Dancing+Script:wght@600&display=swap" rel="stylesheet">
<style>
  :root{
    --canvas:#e4e4e6;
    --slate:#6a6a6c;
    --slate-dark:#4e4e50;
    --paper:#ffffff;
    --ink:#2b2b2b;
    --logo-dark:#5a5a5c;
    --logo-light:#f2f2f2;
    --sign:#2a3a8c;
    --shadow:0 6px 18px rgba(0,0,0,.28);
    --metal:linear-gradient(90deg,#1d1d1d 0%,#5c5c5c 12%,#f4f4f4 32%,#9a9a9a 50%,#ffffff 68%,#6a6a6a 86%,#1d1d1d 100%);
  }
  *{box-sizing:border-box;margin:0;padding:0}
  html,body{width:1200px;height:900px;overflow:hidden}
  body{background:var(--canvas);position:relative;font-family:'Tinos',serif;color:var(--ink)}

  .showcase-title{position:absolute;right:95px;top:30px;font-family:'Raleway',sans-serif;font-weight:300;font-size:46px;color:var(--slate-dark);letter-spacing:.5px}

  .sheet{position:absolute;box-shadow:var(--shadow);overflow:hidden}
  .tab{position:absolute;left:50%;transform:translateX(-50%);height:12px;background:var(--metal)}
  .tab--top{top:0;border-radius:0 0 10px 10px}
  .tab--bottom{bottom:0;border-radius:10px 10px 0 0}

  .wordmark{font-family:'Cinzel',serif;font-weight:400;white-space:nowrap;letter-spacing:.5px}

  /* presentation folder */
  .folder{left:50px;top:225px;width:350px;height:480px;background:var(--slate)}
  .folder .tab{width:140px}
  .folder .wordmark{position:absolute;top:230px;width:100%;text-align:center;font-size:22px;color:var(--logo-light)}
  .folder .web{position:absolute;bottom:18px;width:100%;text-align:center;font-family:'Raleway',sans-serif;font-size:7px;color:#ddd}

  /* letterhead */
  .letterhead{left:425px;top:170px;width:345px;height:500px;background:var(--paper)}
  .letterhead .tab{width:150px}
  .letterhead .wordmark{position:absolute;top:32px;width:100%;text-align:center;font-size:20px;color:var(--logo-dark)}
  .letter{position:absolute;left:38px;top:96px;width:270px;font-size:8.5px;line-height:1.3}
  .letter .recipient{display:flex;gap:18px;margin-bottom:14px}
  .letter p{margin-bottom:9px}
  .letter .signature{font-family:'Dancing Script',cursive;font-weight:600;font-size:15px;color:var(--sign);margin-top:4px}
  .letter-footer{position:absolute;bottom:24px;width:100%;text-align:center;font-size:5.5px;line-height:1.35}
  .letter-footer strong{font-weight:700}

  /* compliments slip */
  .slip{left:795px;top:250px;width:350px;height:210px;background:var(--paper);border-radius:10px}
  .slip .flap{position:absolute;left:0;top:0;width:100%;height:72px;background:var(--slate);border-radius:10px 10px 0 0}
  .slip .flap .tab{width:150px}
  .slip .flap-details{position:absolute;top:26px;width:100%;text-align:center;font-size:5.5px;line-height:1.4;color:#eee}
  .slip .wordmark{position:absolute;top:100px;width:100%;text-align:center;font-size:19px;color:var(--logo-dark)}
  .slip .tab--bottom{width:150px}

  /* business cards */
  .card{width:215px;height:118px;border-radius:10px}
  .card .tab{width:100%;height:10px;left:0;transform:none}
  .card--back{left:945px;top:545px;background:var(--slate)}
  .card--back .wordmark{position:absolute;top:50px;width:100%;text-align:center;font-size:13px;color:var(--logo-light)}
  .card--front{left:805px;top:680px;background:var(--paper)}
  .card--front .wordmark{position:absolute;top:17px;width:100%;text-align:center;font-size:12px;color:var(--logo-dark)}
  .card-person{position:absolute;top:44px;width:100%;text-align:center}
  .card-person .name{font-family:'Cinzel',serif;font-size:7px;color:var(--logo-dark);border-bottom:1px solid #999;display:inline-block;padding:0 12px 2px}
  .card-person .role{font-family:'Cinzel',serif;font-size:4px;letter-spacing:1px;color:#777;margin-top:2px}
  .card-details{position:absolute;top:74px;width:100%;text-align:center;font-size:5px;line-height:1.4}
</style>
</head>
<body>
  <h1 class="showcase-title">Holloway Advisory</h1>

  <section class="sheet folder" aria-label="Presentation folder">
    <div class="tab tab--top"></div>
    <div class="wordmark">Holloway Advisory</div>
    <div class="web">www.holloway-advisory.com</div>
    <div class="tab tab--bottom"></div>
  </section>

  <section class="sheet letterhead" aria-label="Letterhead">
    <div class="tab tab--top"></div>
    <div class="wordmark">Holloway Advisory</div>
    <div class="letter">
      <div class="recipient"><span>To:</span><span>Mr./Mrs. Customer<br>100 Fairview Avenue<br>Hartley<br>NY 55210</span></div>
      <p>Dear Customer,</p>
      <p>Lorem ipsum dolor sit amet, consetetur sadipscing elitr, sed diam nonumy eirmod tempor invidunt ut labore et dolore magna aliquyam erat, sed diam voluptua. At vero eos et accusam et justo duo dolores et ea rebum. Stet clita kasd gubergren, no sea takimata sanctus est. Lorem ipsum dolor sit amet, consetetur sadipscing elitr, sed diam nonumy eirmod tempor invidunt ut labore et dolore magna aliquyam erat.</p>
      <p>Duis autem vel eum iriure dolor in hendrerit in vulputate velit esse molestie consequat, vel illum dolore eu feugiat nulla facilisis at vero eros et accumsan et iusto odio dignissim qui blandit praesent luptatum zzril delenit augue duis dolore te feugait nulla facilisi.</p>
      <p>Nam liber tempor cum soluta nobis eleifend option congue nihil imperdiet doming id quod mazim placerat facer possim assum. Lorem ipsum dolor sit amet, consectetuer adipiscing elit, sed diam nonummy nibh euismod tincidunt ut laoreet dolore magna aliquam erat volutpat. Ut wisi enim ad minim veniam, quis nostrud exerci tation ullamcorper suscipit lobortis nisl ut aliquip ex ea commodo consequat.</p>
      <p>Sincerely,</p>
      <div class="signature">Daniel Marsh</div>
    </div>
    <div class="letter-footer"><strong>Holloway Advisory Pty Ltd</strong><br>Telephone: 0417262938<br>Postal Address : PO Box 482, Elmsford Park, Vic 3187</div>
    <div class="tab tab--bottom"></div>
  </section>

  <section class="sheet slip" aria-label="With compliments slip">
    <div class="flap">
      <div class="tab tab--top"></div>
      <div class="flap-details"><strong>Holloway Advisory Pty Ltd</strong><br>Telephone: 0417262938<br>Postal Address : PO Box 482, Elmsford Park, Vic 3187</div>
    </div>
    <div class="wordmark">Holloway Advisory</div>
    <div class="tab tab--bottom"></div>
  </section>

  <section class="sheet card card--back" aria-label="Business card back">
    <div class="tab tab--top"></div>
    <div class="wordmark">Holloway Advisory</div>
    <div class="tab tab--bottom"></div>
  </section>

  <section class="sheet card card--front" aria-label="Business card front">
    <div class="tab tab--top"></div>
    <div class="wordmark">Holloway Advisory</div>
    <div class="card-person"><div class="name">Daniel Marsh</div><div class="role">Accountant</div></div>
    <div class="card-details"><strong>Holloway Advisory Pty Ltd</strong><br>Telephone: 0417262938<br>Postal Address : PO Box 482, Elmsford Park, Vic 3187</div>
    <div class="tab tab--bottom"></div>
  </section>
</body>
</html>
```